Electrical Contracting business website design

Website needed to help promote an online footprint focused on local customers in my area Gympie, QLD,Australia 4570

I am after a clear website (one where my customer does not get lost or frustrated)
most important is to engage customer to Call now or Request a quote with all the lead details.

Some bread and butter work for us is broken hot water units, electrical faults and renovators

We offer all sorts of services
- smoke alarms
- Test n Tag
- Lighting
- Fans
- A/C
- Design and planning
- safety switches
- underground Power
- Energy efficient solutions
- hot water repair
- Fault finding
- Control / Automation

Target Market(s)

Local Customers, Renovators, Builders, Commercial, Industrial, Domestic

Industry/Entity Type

Electrician

Coding

Coded - Design and coding required

Number of Pages Required

1 page

Colors
f78f20
000000
ec1f27
ffffff

Requirements
Must have
• Easy to use website with clear Contact Information (call now button)
• Ph: 0452916037 24/7
• Email Brightlinepower@mailnest.example
• , Quote request to receive leads and customer info

```html
<!DOCTYPE html>
<html lang="en">
<head>
<meta charset="utf-8">
<title>Brightline Power – Local Electrician</title>
<link href="https://fonts.googleapis.com/css2?family=Titillium+Web:wght@300;400;600;700&display=swap" rel="stylesheet">
<style>
:root{
  --orange:#f78f20;
  --red:#ec1f27;
  --black:#000000;
  --header:#141010;
  --white:#ffffff;
  --grey:#e6e6e6;
  --text:#333333;
}
*{box-sizing:border-box;margin:0;padding:0}
html,body{width:1200px;height:3272px;overflow:hidden}
body{position:relative;background:var(--white);font-family:"Titillium Web",sans-serif;color:var(--text)}
.abs{position:absolute}

/* header */
.site-header{left:0;top:0;width:1200px;height:112px;background:var(--header)}
.brand{left:144px;top:30px;display:flex;align-items:center;gap:10px;color:var(--orange);font-weight:700;font-size:26px;letter-spacing:1px}
.brand-dot{width:36px;height:36px;border-radius:50%;background:var(--red)}
.top-btn{top:22px;height:36px;border:1px solid #555;border-radius:3px;color:#bbb;font-size:13px;display:flex;align-items:center;justify-content:center;gap:8px;white-space:nowrap}
.top-btn.phone{font-size:17px}
.top-btn svg{width:13px;height:13px;fill:#bbb}
.main-nav{top:74px;right:145px;display:flex;gap:46px;font-size:16px;color:#ccc}
.main-nav .active{color:var(--orange)}

/* hero */
.hero{left:0;top:112px;width:1200px;height:590px;background:linear-gradient(180deg,#5b7186 0%,#3d4a3a 30%,#2a2a26 55%,#4b5a2e 80%,#56642f 100%)}
.hero-title{left:0;top:150px;width:1200px;text-align:center;color:var(--white);font-weight:700;font-size:33px;line-height:40px;text-shadow:0 1px 3px rgba(0,0,0,.6)}
.btn-orange{background:linear-gradient(var(--orange),#ee6d12);color:var(--black);font-weight:700;border-radius:3px;display:flex;align-items:center;justify-content:center}
.hero-cta{left:516px;top:242px;width:168px;height:47px;font-size:23px}
.arrow{top:338px;width:48px;height:48px;border-radius:50%;background:rgba(255,255,255,.85);display:flex;align-items:center;justify-content:center}
.arrow svg{width:18px;height:18px;stroke:#222;stroke-width:3;fill:none}
.wave{left:0;top:600px;width:1200px}

/* welcome */
.welcome-bg{left:0;top:700px;width:1200px;height:528px;background:var(--grey)}
.h-small{font-weight:700;font-size:31px;color:var(--black);line-height:1}
.h-red{font-weight:700;font-size:40px;color:var(--red);line-height:1}
.welcome-intro{left:144px;top:771px}
.welcome-name{left:144px;top:815px}
.welcome-copy{left:144px;top:872px;width:424px;font-size:14.4px;line-height:25.6px;color:#222}
.btn-dark{background:var(--black);color:var(--white);font-size:13px;border-radius:2px;display:flex;align-items:center;justify-content:center}
.read-more{left:144px;top:1110px;width:100px;height:39px}

.quick{left:599px;top:775px;width:456px;height:527px;background:radial-gradient(circle at 60% 40%,#e81e2a 0%,#d0101c 70%,#b80a16 100%)}
.quick h2{position:absolute;left:0;top:14px;width:100%;text-align:center;color:var(--white);font-weight:700;font-size:41px}
.field{position:absolute;background:var(--white);border-radius:2px;font-size:13.5px;color:#555;padding:11px 15px}
.field svg{position:absolute;right:14px;top:15px;width:11px;height:11px;stroke:#333;stroke-width:2;fill:none}
.submit{left:168px;top:448px;width:120px;height:51px;font-size:23px}

/* services */
.services-intro{left:0;top:1373px;width:1200px;text-align:center}
.services-name{left:0;top:1421px;width:1200px;text-align:center}
.card{top:1479px;width:218px;height:205px;border:1px solid #444;text-align:center}
.card svg{position:absolute;left:74px;top:30px;width:70px;height:70px;fill:none;stroke:#111;stroke-width:2.4}
.card p{position:absolute;left:30px;right:30px;top:127px;font-size:19px;line-height:24px;color:#222}
.all-services{left:530px;top:1710px;width:140px;height:39px}

/* works */
.works-bg{left:0;top:1830px;width:1200px;height:732px;background:var(--grey)}
.works-title{left:0;top:1905px;width:1200px;text-align:center}
.view-all{left:558px;top:2441px;width:84px;height:39px}

/* contact */
.contact-title{left:0;top:2636px;width:1200px;text-align:center}
.contact-row{left:144px;top:2690px;width:911px;display:flex;justify-content:space-between;font-size:20px;color:#222;white-space:nowrap}
.contact-row span{display:flex;align-items:center;gap:8px}
.contact-row svg{width:16px;height:16px;fill:#222}
.footer-wave{left:0;top:2980px;width:1200px}
.map{left:144px;top:2743px;width:911px;height:398px;background:linear-gradient(135deg,#f2f2ef,#e9ebe6)}
.footer-links{left:144px;top:3180px;font-size:12px;color:#aaa;display:flex;gap:10px}
.copyright{left:144px;top:3212px;font-size:12px;color:#aaa}
.social{top:3200px;width:16px;height:16px;border:2px solid #999;border-radius:3px}
</style>
</head>
<body>

<header class="abs site-header">
  <div class="abs brand"><span class="brand-dot"></span>Brightline Power</div>
  <div class="abs top-btn" style="left:551px;width:136px"><svg viewBox="0 0 16 16"><path d="M2 3h8v2H4v7h7V8h2v6H2z M12 1l3 3-6 6H6V7z"/></svg>Request a Quote</div>
  <div class="abs top-btn" style="left:698px;width:205px;font-size:10.5px"><svg viewBox="0 0 16 16"><path d="M1 3h14v10H1z M1 3l7 6 7-6" stroke="#141010" stroke-width="1"/></svg>Brightlinepower@mailnest.example</div>
  <div class="abs top-btn phone" style="left:911px;width:144px"><svg viewBox="0 0 16 16"><path d="M3 1l3 3-2 2c1 2 3 4 5 5l2-2 3 3-2 3C6 15 1 10 1 3z"/></svg>0452916037</div>
  <nav class="abs main-nav"><span class="active">HOME</span><span>ABOUT US</span><span>SERVICES</span><span>WORKS</span><span>CONTACT US</span></nav>
</header>

<section class="abs hero" role="img" aria-label="Photo of the company work truck towing a scissor lift trailer in a treed yard"></section>
<h1 class="abs hero-title">ETIAM MASSA ELEMENTUM<br>BIBENDUM TELLUS VENENATIS</h1>
<div class="abs btn-orange hero-cta">CONTACT US</div>
<div class="abs arrow" style="left:46px"><svg viewBox="0 0 20 20"><path d="M13 3l-7 7 7 7"/></svg></div>
<div class="abs arrow" style="left:1103px"><svg viewBox="0 0 20 20"><path d="M7 3l7 7-7 7"/></svg></div>
<svg class="abs wave" height="105" viewBox="0 0 1200 105" preserveAspectRatio="none"><path d="M0 92 C150 60 300 15 420 15 C600 15 700 90 900 92 C1030 93 1120 75 1200 58 L1200 105 L0 105Z" fill="#e6e6e6"/></svg>

<section class="abs welcome-bg"></section>
<h2 class="abs h-small welcome-intro">WELCOME TO</h2>
<h2 class="abs h-red welcome-name">BRIGHTLINE POWER</h2>
<p class="abs welcome-copy">Nulla in lorem at massa pellentesque posuere. Nulla tristique posuere molestie. Aliquam erat volutpat. Etiam quis aliquet risus. Duis ornare erat eget magna dapibus, in accumsan quam pharetra. Nam tempus, quam in bibendum vulputate, sapien dolor viverra nisl, vitae euismod elit turpis et nulla. Aliquam erat volutpat. Pellentesque blandit lacus eget nunc faucibus, et tincidunt eros viverra. Phasellus consequat sagittis nisi suscipit feugiat. Cras eget leo sed nunc hendrerit ultricies eu at nisl. Praesent iaculis faucibus urna sit amet lacinia.</p>
<div class="abs btn-dark read-more">READ MORE</div>

<form class="abs quick">
  <h2>QUICK CONTACT</h2>
  <div class="field" style="left:16px;top:77px;width:208px;height:39px">First Name</div>
  <div class="field" style="left:232px;top:77px;width:208px;height:39px">Last Name</div>
  <div class="field" style="left:16px;top:125px;width:208px;height:39px">Phone</div>
  <div class="field" style="left:232px;top:125px;width:208px;height:39px">Email</div>
  <div class="field" style="left:16px;top:173px;width:424px;height:95px">Address</div>
  <div class="field" style="left:16px;top:277px;width:424px;height:39px">Service for<svg viewBox="0 0 12 12"><path d="M2 4l4 4 4-4"/></svg></div>
  <div class="field" style="left:16px;top:325px;width:424px;height:95px">Message</div>
  <div class="abs btn-orange submit">SUBMIT</div>
</form>

<h2 class="abs h-small services-intro">VESTIBULUM CONDIMENTUM RISUS POSUERE</h2>
<h2 class="abs h-red services-name">OUR SERVICES</h2>

<div class="abs card" style="left:144px">
  <svg viewBox="0 0 70 70"><rect x="8" y="22" width="46" height="40" rx="3"/><path d="M15 26v32M22 26v32M29 26v32M36 26v32M43 26v32M50 26v32"/><rect x="12" y="6" width="16" height="10"/><path d="M56 20a6 6 0 0 1 8 0M53 16a11 11 0 0 1 14 0"/></svg>
  <p>Broken hot water units</p>
</div>
<div class="abs card" style="left:375px">
  <svg viewBox="0 0 70 70"><circle cx="35" cy="35" r="32"/><path d="M39 12L25 38h10l-4 20 14-28H35z"/></svg>
  <p style="left:14px;right:14px">Electrical faults and renovators</p>
</div>
<div class="abs card" style="left:606px">
  <svg viewBox="0 0 70 70"><rect x="8" y="22" width="46" height="40" rx="3"/><path d="M15 26v32M22 26v32M29 26v32M36 26v32M43 26v32M50 26v32"/><rect x="12" y="6" width="16" height="10"/><path d="M56 20a6 6 0 0 1 8 0M53 16a11 11 0 0 1 14 0"/></svg>
  <p>Smoke alarms</p>
</div>
<div class="abs card" style="left:837px">
  <svg viewBox="0 0 70 70"><circle cx="32" cy="32" r="30"/><circle cx="32" cy="32" r="20"/><circle cx="32" cy="32" r="11"/><circle cx="32" cy="32" r="4"/><circle cx="56" cy="54" r="9" fill="#fff"/><path d="M56 49v6M56 58v1"/></svg>
  <p>Lighting</p>
</div>
<div class="abs btn-dark all-services">VIEW ALL SERVICES</div>

<section class="abs works-bg"></section>
<h2 class="abs h-red works-title">OUR WORKS</h2>
<div class="abs" style="left:144px;top:1962px;width:217px;height:217px;background:linear-gradient(#7b8ea4,#5a6a3d)" role="img" aria-label="Photo of an outdoor switchboard on a timber pole beside the work truck"></div>
<div class="abs" style="left:144px;top:2192px;width:217px;height:217px;background:linear-gradient(#b9bcbb,#8d8a80)" role="img" aria-label="Photo of switch cabinets installed inside a steel shed"></div>
<div class="abs" style="left:371px;top:1962px;width:458px;height:447px;background:linear-gradient(90deg,#9c968a,#b3ae9f 60%,#8a8a80)" role="img" aria-label="Photo of a power outlet and cable tray mounted on a block wall"></div>
<div class="abs" style="left:838px;top:1962px;width:217px;height:217px;background:linear-gradient(#9ea2a3,#777b7c)" role="img" aria-label="Photo of conduits running into a wall mounted box on a metal wall"></div>
<div class="abs" style="left:838px;top:2192px;width:217px;height:217px;background:linear-gradient(#8fa0b2,#9b7a5e)" role="img" aria-label="Photo of a power pole with meter box on a dirt site"></div>
<div class="abs btn-dark view-all">VIEW ALL</div>

<h2 class="abs h-red contact-title">CONTACT US</h2>
<div class="abs contact-row">
  <span><svg viewBox="0 0 16 16"><path d="M8 0a5 5 0 0 0-5 5c0 4 5 11 5 11s5-7 5-11a5 5 0 0 0-5-5zm0 7a2 2 0 1 1 0-4 2 2 0 0 1 0 4z"/></svg>Ridgeway Road Kellmont, Eastvale 9012</span>
  <span><svg viewBox="0 0 16 16"><path d="M3 1l3 3-2 2c1 2 3 4 5 5l2-2 3 3-2 3C6 15 1 10 1 3z"/></svg>0452916037</span>
  <span><svg viewBox="0 0 16 16"><path d="M1 3h14v10H1z"/><path d="M1 3l7 6 7-6" stroke="#fff" stroke-width="1.4" fill="none"/></svg>Brightlinepower@mailnest.example</span>
</div>
<svg class="abs footer-wave" height="292" viewBox="0 0 1200 292" preserveAspectRatio="none"><path d="M0 88 C250 170 500 180 750 120 C950 70 1100 30 1200 12 L1200 292 L0 292Z" fill="#000"/></svg>
<div class="abs map" role="img" aria-label="Street map of the business location"></div>

<footer>
  <nav class="abs footer-links"><span>Home</span><span>|</span><span>About Us</span><span>|</span><span>Services</span><span>|</span><span>Works</span><span>|</span><span>Contact Us</span></nav>
  <p class="abs copyright">Copyright © 2019 Brightline Power. All rights reserved.</p>
  <span class="abs social" style="left:997px" aria-label="Social link"></span>
  <span class="abs social" style="left:1039px" aria-label="Social link"></span>
</footer>

</body>
</html>
```